Trade Alert Service needs Youtube thumbnail / channel design

I'm about to set up a Youtube channel which gives real-time trade alerts to earn passive income. I'm looking for a Youtube channel design to include thumbnail and other associated visuals for the channel.
The trade alerts will be focused around selling cash-secured put options on US equities, and directed at people who want investing advice / tips for getting out of the rat race. I'd like the theme to be somewhat serious / credible, without too many eye-popping neon colours like all the other cheap trade alert videos / day trading videos on Youtube. Happy for you to use your experience if you think otherwise though, as you're the designer, not me!

Target Market(s)

Option Traders, Value Investors, People who want passive income

Industry/Entity Type

Finance

Logo Text

Bramblewick Quarter Guild

Requirements
Must have
• All relevant Youtube visuals so that I can upload them to the Youtube channel - all visuals required by Youtube Studio upload within the channel creation page.
A logo so that I can append it to Powerpoint presentations
Nice to have
• A blank Powerpoint slide template showing the logo would be great in chosen colour scheme

```html
<!DOCTYPE html>
<html lang="en">
<head>
<meta charset="utf-8">
<title>Trading and Investing – Thumbnail</title>
<link rel="stylesheet" href="https://fonts.googleapis.com/css2?family=Montserrat:ital,wght@1,800;1,900&display=swap">
<style>
  :root {
    --page-bg: #ffffff;
    --navy-deep: #0c1731;
    --navy: #15284f;
    --navy-band: #1f3b6b;
    --navy-light: #27487f;
    --orange: #e8860f;
    --white: #ffffff;
    --photo-warm: #8a6440;
    --photo-mid: #3d3631;
    --photo-dark: #1a1a1e;
    --photo-desk: #d9d4cf;
  }
  html, body {
    margin: 0;
    padding: 0;
    width: 1200px;
    height: 1000px;
    overflow: hidden;
    background: var(--page-bg);
  }
  .thumbnail {
    position: absolute;
    left: 69px;
    top: 194px;
    width: 1046px;
    height: 587px;
  }
  .thumbnail svg { display: block; }
  .headline {
    font-family: "Montserrat", Arial, sans-serif;
    font-style: italic;
    font-weight: 800;
  }
  .headline-white { fill: var(--white); }
  .headline-orange { fill: var(--orange); }
  .headline-big { font-weight: 900; }
</style>
</head>
<body>
  <div class="thumbnail">
    <svg width="1046" height="587" viewBox="0 0 1046 587" xmlns="http://www.w3.org/2000/svg">
      <defs>
        <linearGradient id="bgNavy" x1="0" y1="0" x2="1" y2="1">
          <stop offset="0" stop-color="var(--navy)"/>
          <stop offset="1" stop-color="var(--navy-deep)"/>
        </linearGradient>
        <linearGradient id="photoTone" x1="1" y1="0" x2="0" y2="1">
          <stop offset="0" stop-color="var(--photo-warm)"/>
          <stop offset="0.45" stop-color="var(--photo-mid)"/>
          <stop offset="0.8" stop-color="var(--photo-dark)"/>
          <stop offset="1" stop-color="var(--photo-desk)"/>
        </linearGradient>
      </defs>

      <!-- background field -->
      <rect class="field" width="1046" height="587" fill="url(#bgNavy)"/>

      <!-- diagonal accent bands -->
      <polygon class="accent-band" points="0,0 120,0 0,200" fill="var(--navy-light)" opacity="0.55"/>
      <polygon class="accent-band" points="300,0 520,0 180,587 0,587 0,500" fill="var(--navy-band)" opacity="0.45"/>
      <polygon class="accent-band" points="470,0 560,0 260,587 170,587" fill="var(--navy-deep)" opacity="0.55"/>
      <polygon class="accent-band" points="400,587 700,587 560,470" fill="var(--navy-band)" opacity="0.6"/>

      <!-- photo area -->
      <polygon class="photo-area" role="img" aria-label="Photo of a person typing on a laptop showing a trading dashboard with candlestick charts, beside a coffee cup"
               points="593,0 1046,0 1046,587 701,587 358,392" fill="url(#photoTone)"/>

      <!-- white chevron divider -->
      <polyline class="divider" points="593,0 358,392 701,587" fill="none" stroke="var(--white)" stroke-width="5"/>

      <!-- headline -->
      <text class="headline headline-white" x="58" y="181" font-size="47">TRADING AND</text>
      <text class="headline headline-orange" x="55" y="237" font-size="47">INVESTING</text>

      <!-- banner: our way to -->
      <polygon class="banner-navy" points="100,276 503,276 478,346 75,346" fill="var(--navy-band)"/>
      <text class="headline headline-white" x="83" y="326" font-size="48">OUR WAY TO</text>

      <!-- banner: financial -->
      <polygon class="banner-orange" points="82,346 672,346 640,431 40,431" fill="var(--orange)"/>
      <text class="headline headline-white headline-big" x="90" y="416" font-size="82">FINANCIAL</text>

      <!-- banner: freedom -->
      <polygon class="banner-navy" points="230,431 643,431 625,492 189,492" fill="var(--navy-band)"/>
      <text class="headline headline-white" x="279" y="478" font-size="46">FREEDOM</text>
    </svg>
  </div>
</body>
</html>
```